Re-Design Qarnelo.com make it more professional looking

We want to re-design this website, we are currently not happy with existing design. Some of the design examples are listed below.

https://lumbek.com/
https://www.fastroe.com/
https://www.kelvaro.com/projects/
https://www.brightmoss.com/

The content on the website is final, there will be no change in the content. We just need to re-design the site. Features page on the site is very important and need to be layout very well.

Industry/Entity Type

It Professional

Number of Pages Required

4 page

Font styles to use
Sans Serif

Requirements
Must have
• Professional look and design like the examples i quoted above and a nice color theme. I do not have preferences but i like the fastroe.com and lumbek.com

```html
<!DOCTYPE html>
<html lang="en">
<head>
<meta charset="utf-8">
<title>Qarnelo – Project Management for Digital Agencies</title>
<link rel="stylesheet" href="https://fonts.googleapis.com/css2?family=Open+Sans:wght@300;400;600;700&family=Montserrat:wght@400;600;700&display=swap">
<style>
:root{
  --orange:#f7a21b;
  --orange-dark:#e58f0a;
  --blue:#2c8fd6;
  --blue-light:#4aa8ea;
  --ink:#2f3338;
  --text:#5b6168;
  --muted:#8c9298;
  --dark:#24282d;
  --dark-2:#2e3338;
  --footer:#33383e;
  --footer-bottom:#2a2e33;
  --line:#e4e6e8;
  --white:#ffffff;
  --pale:#f4f5f6;
}
*{box-sizing:border-box;margin:0;padding:0}
html,body{width:1200px;height:2608px;overflow:hidden}
body{font-family:"Open Sans",Arial,sans-serif;color:var(--text);background:var(--white);position:relative}
section,header,footer{position:absolute;left:0;width:1200px;overflow:hidden}

/* Hero */
.hero{top:0;height:560px}
.hero-photo{position:absolute;inset:0;background:linear-gradient(160deg,#5d5a55 0%,#3f3d3a 35%,#8c8a85 60%,#2f2d2b 100%)}
.hero-shade{position:absolute;inset:0;background:linear-gradient(180deg,rgba(20,20,22,.55),rgba(20,20,22,.25) 60%,rgba(20,20,22,.45))}
.nav{position:absolute;top:22px;left:0;width:100%;height:50px}
.brand{position:absolute;left:78px;top:6px;display:flex;align-items:center;gap:10px;font-family:"Montserrat",sans-serif;font-weight:700;font-size:30px;color:var(--orange)}
.brand-dot{width:14px;height:14px;border-radius:50%;background:var(--orange)}
.menu{position:absolute;left:500px;top:8px;display:flex;gap:18px;list-style:none}
.menu li{font-size:14px;color:var(--white);padding:7px 16px;border-radius:18px}
.menu li.active{background:var(--orange)}
.login{position:absolute;left:1030px;top:8px;font-size:14px;color:var(--white);border:1px solid rgba(255,255,255,.8);border-radius:4px;padding:6px 22px}
.hero-copy{position:absolute;top:140px;width:100%;text-align:center;color:var(--white)}
.hero-copy h1{font-weight:400;font-size:38px;letter-spacing:.2px}
.hero-copy p{font-size:16px;margin-top:10px;opacity:.9}
.signup{position:absolute;top:312px;left:364px;width:472px;height:48px;display:flex;border-radius:24px;background:var(--white);overflow:hidden}
.signup span{flex:1;font-size:14px;color:var(--muted);padding:14px 22px}
.signup b{width:170px;background:var(--orange);color:var(--white);font-weight:600;font-size:14px;display:flex;align-items:center;justify-content:center}

/* Slider */
.slider{top:560px;height:448px;background:linear-gradient(180deg,#eceeef,#f8f9f9)}
.laptop-shot{position:absolute;left:180px;top:40px;width:360px;height:360px;border-radius:6px;background:linear-gradient(150deg,#cfd6dc,#e9eef2 55%,#bfc6cc)}
.slide-copy{position:absolute;left:634px;top:158px;width:380px}
.slide-copy h2{font-weight:400;font-size:28px;line-height:1.3;color:var(--ink)}
.btn-blue{display:inline-block;margin-top:18px;background:var(--blue);color:var(--white);font-size:14px;font-weight:600;padding:10px 24px;border-radius:20px}
.arrow{position:absolute;top:200px;width:30px;height:40px}
.arrow.left{left:28px}.arrow.right{right:28px}

/* Features */
.features{top:1008px;height:592px;background:linear-gradient(180deg,#2b2f34,#1f2226)}
.features .eyebrow{position:absolute;top:62px;width:100%;text-align:center;font-size:12px;letter-spacing:2px;color:#aab0b6}
.features h2{position:absolute;top:84px;width:100%;text-align:center;font-weight:600;font-size:26px;color:var(--blue-light)}
.feature-grid{position:absolute;top:150px;left:150px;width:900px;display:grid;grid-template-columns:repeat(4,1fr);row-gap:32px;list-style:none}
.feature{display:flex;align-items:center;gap:14px;color:var(--white);font-size:14px;line-height:1.35}
.feature svg{flex:none}
.integrations{position:absolute;top:400px;width:100%;text-align:center;font-size:12px;color:#a2a8ae}
.integrations::before,.integrations::after{content:"";display:inline-block;width:220px;height:1px;background:#4a5057;vertical-align:middle;margin:0 16px}
.partners{position:absolute;top:460px;left:180px;width:860px;display:flex;justify-content:space-between;align-items:center;list-style:none}
.partner{display:flex;align-items:center;gap:8px;color:#d6d9dc;font-size:20px;font-weight:600}
.partner i{width:18px;height:18px;background:#d6d9dc;border-radius:50%}
.socials{display:flex;gap:10px}
.socials i{width:28px;height:28px;border-radius:50%;background:#d6d9dc;display:block}

/* Testimonial */
.testimonial{top:1600px;height:480px;background:var(--white)}
.avatar{position:absolute;left:552px;top:180px;width:96px;height:96px;border-radius:50%;background:linear-gradient(160deg,#9aa3ab,#5e666e);border:3px solid var(--white);box-shadow:0 0 0 1px var(--line)}
.quote{position:absolute;left:220px;top:300px;width:760px;text-align:center;font-size:14px;line-height:1.65;color:var(--text)}
.author{position:absolute;top:404px;width:100%;text-align:center}
.author b{display:block;font-size:15px;color:var(--ink);font-weight:600}
.author span{font-size:13px;color:var(--muted)}
.testimonial .arrow{top:258px}

/* CTA */
.cta{top:2080px;height:232px;background:var(--pale);text-align:center}
.cta h2{margin-top:52px;font-weight:400;font-size:28px;color:var(--blue)}
.cta p{margin-top:6px;font-size:14px;color:var(--orange-dark)}
.btn-orange{display:inline-block;margin-top:22px;background:var(--orange);color:var(--white);font-size:14px;font-weight:600;padding:12px 30px;border-radius:4px}

/* Footer */
.site-footer{top:2312px;height:248px;background:var(--footer);color:#c9cdd1}
.footer-cols{position:absolute;top:42px;left:150px;display:grid;grid-template-columns:150px 180px 230px 280px;gap:40px}
.footer-cols h4{font-size:14px;color:var(--white);font-weight:600;margin-bottom:14px}
.footer-cols ul{list-style:none;font-size:12.5px;line-height:1.75}
.footer-cols li.current{color:var(--blue-light)}
.phone{font-size:20px;color:var(--white);font-weight:300}
.footer-cols .mail{font-size:12.5px;margin-bottom:14px}
.follow{display:flex;gap:8px;margin-top:6px}
.follow i{width:20px;height:20px;border-radius:3px;background:#aab0b6;display:block}
.follow i:first-child{background:var(--blue)}
.blog li{margin-bottom:8px;line-height:1.4}
.blog li.hl{color:var(--blue-light)}
.blog .more{color:var(--white);font-size:12.5px}
.footer-bar{top:2560px;height:48px;background:var(--footer-bottom);color:#9aa0a6;font-size:12px}
.footer-bar p{position:absolute;left:150px;top:16px}
.to-top{position:absolute;left:1010px;top:10px;width:28px;height:28px;border-radius:50%;background:var(--orange)}
</style>
</head>
<body>

<header class="hero">
  <div class="hero-photo" role="img" aria-label="Photo of a desk with a notebook, a hand sketching a brand plan and a cup of coffee"></div>
  <div class="hero-shade"></div>
  <nav class="nav">
    <div class="brand"><span class="brand-dot"></span>qarnelo</div>
    <ul class="menu">
      <li class="active">Home</li><li>Features</li><li>Pricing</li><li>About Us</li><li>Contact Us</li>
    </ul>
    <span class="login">Login</span>
  </nav>
  <div class="hero-copy">
    <h1>SEO is About Organize, Collaborate and Deliver !</h1>
    <p>It is a long established fact that a reader will be distracted by the readable content of a page when looking.</p>
  </div>
  <div class="signup"><span>Enter your business email</span><b>Get started for free</b></div>
</header>

<section class="slider">
  <svg class="arrow left" viewBox="0 0 30 40"><path d="M20 6 8 20l12 14" fill="none" stroke="#3a3f44" stroke-width="3"/></svg>
  <div class="laptop-shot" role="img" aria-label="Laptop showing the Qarnelo project dashboard"></div>
  <div class="slide-copy">
    <h2>Best Project Management Tool for Digital Agencies</h2>
    <span class="btn-blue">Start Your Free Trial</span>
  </div>
  <svg class="arrow right" viewBox="0 0 30 40"><path d="M10 6l12 14-12 14" fill="none" stroke="#3a3f44" stroke-width="3"/></svg>
</section>

<section class="features">
  <p class="eyebrow">FEATURES</p>
  <h2>The Components You Need, Together on One Tool</h2>
  <ul class="feature-grid">
    <li class="feature"><svg width="40" height="40" viewBox="0 0 40 40"><circle cx="20" cy="20" r="19" fill="none" stroke="#fff" stroke-width="1.5"/><rect x="13" y="13" width="14" height="14" fill="none" stroke="#fff" stroke-width="2"/></svg>Project<br>Management</li>
    <li class="feature"><svg width="40" height="40" viewBox="0 0 40 40"><circle cx="20" cy="20" r="19" fill="none" stroke="#fff" stroke-width="1.5"/><path d="M12 26h16M14 24v-6M20 24v-10M26 24v-8" stroke="#fff" stroke-width="2"/></svg>Collaborative<br>Dashboard</li>
    <li class="feature"><svg width="40" height="40" viewBox="0 0 40 40"><circle cx="20" cy="20" r="19" fill="none" stroke="#fff" stroke-width="1.5"/><circle cx="20" cy="16" r="4" fill="#fff"/><path d="M13 28c1-5 13-5 14 0" fill="#fff"/></svg>User-level<br>Interface</li>
    <li class="feature"><svg width="40" height="40" viewBox="0 0 40 40"><circle cx="20" cy="20" r="19" fill="none" stroke="#fff" stroke-width="1.5"/><rect x="14" y="19" width="12" height="9" fill="#fff"/><path d="M16 19v-3a4 4 0 0 1 8 0v3" fill="none" stroke="#fff" stroke-width="2"/></svg>Password<br>Manager</li>
    <li class="feature"><svg width="40" height="40" viewBox="0 0 40 40"><circle cx="20" cy="20" r="19" fill="none" stroke="#fff" stroke-width="1.5"/><path d="M13 20l5 5 9-10" fill="none" stroke="#fff" stroke-width="2"/></svg>Task<br>Management</li>
    <li class="feature"><svg width="40" height="40" viewBox="0 0 40 40"><circle cx="20" cy="20" r="19" fill="none" stroke="#fff" stroke-width="1.5"/><circle cx="16" cy="17" r="3" fill="#fff"/><circle cx="25" cy="17" r="3" fill="#fff"/><path d="M11 27c1-4 9-4 10 0M20 27c1-4 9-4 10 0" fill="#fff"/></svg>Client<br>Management</li>
    <li class="feature"><svg width="40" height="40" viewBox="0 0 40 40"><circle cx="20" cy="20" r="19" fill="none" stroke="#fff" stroke-width="1.5"/><rect x="12" y="13" width="16" height="12" fill="none" stroke="#fff" stroke-width="2"/><path d="M17 28h6" stroke="#fff" stroke-width="2"/></svg>Customer<br>Portal</li>
    <li class="feature"><svg width="40" height="40" viewBox="0 0 40 40"><circle cx="20" cy="20" r="19" fill="none" stroke="#fff" stroke-width="1.5"/><rect x="12" y="15" width="16" height="11" rx="1" fill="none" stroke="#fff" stroke-width="2"/><path d="M12 19h16" stroke="#fff" stroke-width="2"/></svg>Billing<br>Management</li>
    <li class="feature"><svg width="40" height="40" viewBox="0 0 40 40"><circle cx="20" cy="20" r="19" fill="none" stroke="#fff" stroke-width="1.5"/><path d="M15 28V12l11 4-11 4" fill="none" stroke="#fff" stroke-width="2"/></svg>Milestones<br>Management</li>
    <li class="feature"><svg width="40" height="40" viewBox="0 0 40 40"><circle cx="20" cy="20" r="19" fill="none" stroke="#fff" stroke-width="1.5"/><circle cx="20" cy="15" r="3" fill="#fff"/><circle cx="13" cy="22" r="2.5" fill="#fff"/><circle cx="27" cy="22" r="2.5" fill="#fff"/><path d="M15 28c1-5 9-5 10 0" fill="#fff"/></svg>Team<br>Management</li>
    <li class="feature"><svg width="40" height="40" viewBox="0 0 40 40"><circle cx="20" cy="20" r="19" fill="none" stroke="#fff" stroke-width="1.5"/><path d="M12 15h7l2 2h7v10H12z" fill="none" stroke="#fff" stroke-width="2"/></svg>File<br>Manager</li>
    <li class="feature"><svg width="40" height="40" viewBox="0 0 40 40"><circle cx="20" cy="20" r="19" fill="none" stroke="#fff" stroke-width="1.5"/><path d="M14 14h12M14 20h12M14 26h8" stroke="#fff" stroke-width="2"/></svg>Task<br>Management</li>
  </ul>
  <p class="integrations">Integrated with some of the Most Popular Apps You Already use</p>
  <ul class="partners">
    <li class="partner"><i></i>Drivelane</li>
    <li class="partner">Ledgerly</li>
    <li class="partner"><i></i>Northgrid</li>
    <li class="partner">Cloudvale</li>
    <li class="partner"><i></i>Boxwell</li>
    <li class="socials"><i></i><i></i><i></i></li>
  </ul>
</section>

<section class="testimonial">
  <svg class="arrow left" viewBox="0 0 30 40"><path d="M20 6 8 20l12 14" fill="none" stroke="#9aa0a6" stroke-width="2"/></svg>
  <div class="avatar" role="img" aria-label="Portrait of the customer giving the testimonial"></div>
  <p class="quote">We tested different project management tools, but none of them came close to the simplicity and power of Qarnelo. It keeps every client, task and deadline in one place, so our whole team knows what comes next. We now deliver projects faster and spend far less time on status meetings and long email threads every week.</p>
  <div class="author"><b>Dorian Hale</b><span>Project Manager at Brightwave</span></div>
  <svg class="arrow right" viewBox="0 0 30 40"><path d="M10 6l12 14-12 14" fill="none" stroke="#9aa0a6" stroke-width="2"/></svg>
</section>

<section class="cta">
  <h2>Get started on Qarnelo</h2>
  <p>Share your experience with a unique 1 month of premium access for free</p>
  <span class="btn-orange">Get My 30 Day Free Trial</span>
</section>

<footer class="site-footer">
  <div class="footer-cols">
    <div>
      <h4>Quick Link</h4>
      <ul><li>Home</li><li class="current">About Us</li><li>Features</li><li>Pricing</li><li>Contact Us</li><li>Sitemap</li></ul>
    </div>
    <div>
      <h4>Resources</h4>
      <ul><li>Testimonials</li><li>3rd Party Apps</li><li>Newsletters</li><li>Support &amp; Help</li><li>Privacy Policy</li><li>Tos and Policy</li></ul>
    </div>
    <div>
      <h4>Help &amp; Support</h4>
      <p class="phone">Call Us: +1-555-010-4821</p>
      <p class="mail">hello@qarnelo.com</p>
      <h4>Follow Us</h4>
      <div class="follow"><i></i><i></i><i></i><i></i></div>
    </div>
    <div>
      <h4>Latest in Qarnelo Blog</h4>
      <ul class="blog">
        <li>Combating Scope Creep: Practical Steps for Agency Teams</li>
        <li class="hl">Seven Habits That Keep Remote Project Teams Aligned</li>
        <li>How to Build an Honest and Clear Client Reporting Routine</li>
        <li class="more">» View All Blog</li>
      </ul>
    </div>
  </div>
</footer>
<footer class="site-footer footer-bar">
  <p>© 2016, Qarnelo by Norvane Infotech Pvt. Ltd. All Rights Reserved.</p>
  <svg class="to-top" viewBox="0 0 28 28"><circle cx="14" cy="14" r="14" fill="#f7a21b"/><path d="M9 16l5-5 5 5" fill="none" stroke="#fff" stroke-width="2"/></svg>
</footer>

</body>
</html>
```